Business Card Design for a Private Label Pet Company

We need a business card design for our family-owned company, Harbor Paw Works (www.harborpawworks-example.com), out of St. Louis, MO. We provide turnkey private label solutions for retailers, Cartwell sellers and other brands who want to provide high quality, natural, Made in the USA pet products to their customers. Our customer are worldwide and range from the US to the UK to Vietnam and beyond. We offer private label for dozens of pet products including grooming products (shampoos, conditioners, colognes, ear and eye washes, mouthwash, etc.), all meat treats, supplements, and specialty products (pet stain and odor cleaner, anti-chew spray, etc.). We would like to see designs that use the colors, fonts and logos (see variations) within our brand guidelines and fit with the look and feel from our website.

Target Market(s)

Pet Store Owners, Cartwell Sellers, Pet Brand Marketers

Industry/Entity Type

Pet

Contact Information for Business Card

Lyle Dorsett
CEO
Harbor Paw Works
5817 Wexmoor Commerce Lane
St. Louis, MO 63188
office: 314.555.0182
mobile: 770.555.0139
email: lyle@harborpawworks-example.com

Colors

Designer to choose colors to be used in the design.

Requirements
Must have
• Need to follow the brand guidelines attached for colors, fonts and logos
• Need to use the logos attached (or a variation) with our without the tagline
• Name, title, phone (office and mobil), email, address on the business card
• Clean professional look and feel that says: high quality natural pet products, high quality service, made in the USA
Nice to have
• Made in the USA is a big positive in our industry and we are very proud of it. There is an attached icon from our website. The designer can get creative here as they wish.
• I do like using color for pop. Just don't like lots of bright, loud colors.
Should not have
• lots of bright, loud colors
• overwhelming to the reader
• crowded

```html
<!DOCTYPE html>
<html lang="en">
<head>
<meta charset="utf-8">
<title>Harbor Paw Works – Business Card</title>
<link href="https://fonts.googleapis.com/css2?family=Arimo:wght@400;700&family=Open+Sans:wght@400&display=swap" rel="stylesheet">
<style>
  :root {
    --backdrop: #676767;
    --card: #ffffff;
    --teal: #48625f;
    --leaf: #5d7d2e;
    --ink: #222222;
    --rule: #c9c9c9;
  }
  * { margin: 0; padding: 0; box-sizing: border-box; }
  html, body { width: 1200px; height: 802px; overflow: hidden; }
  body {
    background: var(--backdrop);
    position: relative;
    font-family: "Arimo", Arial, sans-serif;
    color: var(--ink);
  }
  .card {
    position: absolute;
    top: 274px;
    width: 443px;
    height: 265px;
    background: var(--card);
  }
  .card--front { left: 134px; }
  .card--back { left: 624px; }

  .side-band {
    position: absolute; left: 0; top: 0; bottom: 0;
    width: 37px; background: var(--teal);
  }
  .side-stripe {
    position: absolute; left: 37px; top: 0; bottom: 0;
    width: 5px; background: var(--leaf);
  }
  .person-name {
    position: absolute; left: 71px; top: 43px;
    font-size: 16.5px; font-weight: 700; color: var(--teal);
    letter-spacing: 0.2px;
  }
  .person-title {
    position: absolute; left: 71px; top: 62px;
    font-size: 13px;
  }
  .divider {
    position: absolute; left: 71px; width: 278px;
    height: 1px; background: var(--rule);
  }
  .divider--top { top: 88px; }
  .divider--bottom { top: 172px; }
  .contact-list {
    position: absolute; left: 71px; top: 96px;
    list-style: none; font-size: 12.5px; line-height: 15.8px;
  }
  .contact-list li { display: flex; align-items: center; gap: 4px; }
  .contact-icon { width: 10px; height: 10px; fill: var(--teal); flex: none; }
  .company-name {
    position: absolute; left: 71px; top: 180px;
    font-size: 13.5px; font-weight: 700; color: var(--leaf);
  }
  .company-address {
    position: absolute; left: 71px; top: 197px;
    font-size: 12.8px; line-height: 16px; font-style: normal;
  }

  .brand-wordmark {
    position: absolute; left: 0; right: 0; top: 76px;
    display: flex; justify-content: center; align-items: center; gap: 9px;
    font-size: 31px; font-weight: 700; color: var(--teal);
    letter-spacing: 0.5px;
  }
  .brand-dot {
    width: 14px; height: 14px; border-radius: 50%; background: var(--leaf);
  }
  .brand-tagline {
    position: absolute; left: 0; right: 0; top: 162px;
    text-align: center; font-size: 12.5px; color: var(--teal);
    letter-spacing: 0.4px;
  }
  .web-line {
    position: absolute; left: 41px; right: 40px; top: 205px;
    display: flex; align-items: center; gap: 3px;
    font-family: "Open Sans", Arial, sans-serif;
    font-size: 12.3px; color: var(--leaf);
  }
  .web-line::before, .web-line::after {
    content: ""; flex: 1; height: 1px; background: var(--leaf);
  }
</style>
</head>
<body>
  <section class="card card--front">
    <div class="side-band"></div>
    <div class="side-stripe"></div>
    <h1 class="person-name">LYLE DORSETT</h1>
    <p class="person-title">CEO</p>
    <div class="divider divider--top"></div>
    <ul class="contact-list">
      <li>
        <svg class="contact-icon" viewBox="0 0 10 10"><path d="M0 3.5C0 1.5 2.5 1 5 1s5 .5 5 2.5L8.2 4.2 7 3H3L1.8 4.2Z"/><path d="M2.5 5 3.5 3.8h3L7.5 5 8.5 9h-7Z"/></svg>
        314.555.0182
      </li>
      <li>
        <svg class="contact-icon" viewBox="0 0 10 10"><path d="M2.8 0h4.4c.5 0 .8.3.8.8v8.4c0 .5-.3.8-.8.8H2.8c-.5 0-.8-.3-.8-.8V.8c0-.5.3-.8.8-.8Zm.4 1.2v6.6h3.6V1.2Z"/></svg>
        770.555.0139
      </li>
      <li>
        <svg class="contact-icon" viewBox="0 0 10 10"><path d="M0 2h10v6H0Zm1 .8L5 5.6 9 2.8Z" fill-rule="evenodd"/></svg>
        lyle@harborpawworks-example.com
      </li>
      <li>
        <svg class="contact-icon" viewBox="0 0 10 10"><circle cx="5" cy="5" r="4.6"/><path d="M3 2.5 4.8 3.3 4 5 5.5 6.5 5 8.5 3 6Z M6.5 1.8 8 3 7 4Z" fill="#fff"/></svg>
        www.harborpawworks-example.com
      </li>
    </ul>
    <div class="divider divider--bottom"></div>
    <h2 class="company-name">HARBOR PAW WORKS</h2>
    <address class="company-address">5817 Wexmoor Commerce Lane<br>St. Louis, MO 63188</address>
  </section>

  <section class="card card--back">
    <div class="brand-wordmark"><span>HARBOR PAW WORKS</span><span class="brand-dot"></span></div>
    <p class="brand-tagline">TURNKEY PRIVATE LABEL PARTNER</p>
    <p class="web-line">www.harborpawworks-example.com</p>
  </section>
</body>
</html>
```